Web Header needed for an inspirational coaching company's website - ongoing work

We need a beautifully designed web header to replace my current one at my homepage on my website www.brekavol.com
There will be continuous work required for various creative work in the future if your work is selected.
I work with corporate professionals and executives to bring clarity and joy back to their career. It needs to be elegant, sophisticated, intelligent, but friendly and inspiring at the same time.
Brief and the sample header size are attached in my files
Thank you!
Target Market(s)
Corporate profesionals and executives
Industry/Entity Type
It Company
Colors
Designer to choose colors to be used in the design.
Look and feel
Each slider illustrates characteristics of the customer's brand and the style your logo design should communicate.

```html
<!DOCTYPE html>
<html lang="en">
<head>
<meta charset="UTF-8">
<title>Bring Clarity to Your Career – Header</title>
<link rel="stylesheet" href="https://fonts.googleapis.com/css2?family=Great+Vibes&display=swap">
<style>
  :root {
    --teal-bright: #5fe3f7;
    --teal-light: #a8f2fc;
    --teal-mid: #1aa9c4;
    --teal-deep: #0a5f73;
    --teal-dark: #052e38;
    --ink: #0c0c0c;
    --coral: #ec5b26;
    --white: #ffffff;
  }
  html, body {
    margin: 0;
    padding: 0;
    width: 1200px;
    height: 539px;
    overflow: hidden;
    background: var(--teal-dark);
  }
  .header-banner {
    position: relative;
    width: 1200px;
    height: 539px;
    overflow: hidden;
  }
  .backdrop {
    position: absolute;
    inset: 0;
    background:
      radial-gradient(ellipse 180px 90px at 250px 60px, var(--teal-light), transparent 70%),
      radial-gradient(ellipse 150px 120px at 610px 150px, var(--white), transparent 70%),
      radial-gradient(ellipse 200px 80px at 1020px 50px, var(--teal-light), transparent 70%),
      radial-gradient(ellipse 140px 220px at 120px 330px, var(--teal-dark), transparent 75%),
      radial-gradient(ellipse 130px 200px at 1040px 300px, var(--ink), transparent 75%),
      radial-gradient(ellipse 90px 200px at 700px 380px, var(--teal-deep), transparent 75%),
      radial-gradient(ellipse 160px 120px at 1170px 200px, var(--teal-bright), transparent 75%),
      linear-gradient(180deg, var(--teal-bright) 0%, var(--teal-mid) 45%, var(--teal-deep) 100%);
  }
  .portrait {
    position: absolute;
    left: 188px;
    top: 152px;
    width: 292px;
    height: 387px;
    border-radius: 120px 120px 0 0;
    background: linear-gradient(180deg, var(--ink) 0%, #2a1a14 45%, var(--coral) 100%);
  }
  .tagline {
    position: absolute;
    left: 604px;
    top: 226px;
    margin: 0;
    font-family: "Great Vibes", cursive;
    font-weight: 400;
    font-size: 92px;
    line-height: 104px;
    color: var(--white);
    text-shadow:
      1px 1px 0 #c9d6da,
      2px 3px 3px rgba(0, 0, 0, 0.55);
  }
  .tagline span {
    display: block;
  }
</style>
</head>
<body>
  <header class="header-banner">
    <div class="backdrop" role="img" aria-label="Softly blurred teal office scene with silhouettes of people"></div>
    <div class="portrait" role="img" aria-label="Portrait of the coach, smiling, with long dark hair and an orange sleeveless top"></div>
    <h1 class="tagline">
      <span>Bring Clarity</span>
      <span>to Your Career</span>
    </h1>
  </header>
</body>
</html>
```